Business card design for Bront Engineering Qavo

We need a new business card design along with all the necessary to place an order. The company is Bront Engineering Qavo and we recently updated our logo.

```html
<!DOCTYPE html>
<html lang="en">
<head>
<meta charset="utf-8">
<title>Bront Engineering Qavo – Business Card</title>
<link rel="stylesheet" href="https://fonts.googleapis.com/css2?family=Montserrat:wght@600;700&family=Nunito:wght@400;600&display=swap">
<style>
  :root {
    --page: #ffffff;
    --card: #1c1c1c;
    --grey: #9c9b97;
    --grey-light: #a8a8a8;
    --rule: #8a8a8a;
    --white: #ffffff;
    --yellow: #e5c400;
  }
  * { margin: 0; padding: 0; box-sizing: border-box; }
  html, body {
    width: 1200px; height: 1200px; overflow: hidden;
    background: var(--page);
  }
  .card {
    position: absolute; left: 181px; width: 845px; height: 483px;
    background: var(--card);
  }
  .card--front { top: 94px; }
  .card--back { top: 630px; }

  .brand {
    position: absolute; display: flex; align-items: center; gap: 16px;
    font-family: "Montserrat", sans-serif; font-weight: 700;
    color: var(--grey); text-transform: uppercase;
  }
  .brand__mark { width: 34px; height: 34px; background: var(--yellow); flex: none; }
  .brand__mark--grey { background: var(--grey); }
  .brand__name { font-size: 30px; line-height: 1.1; letter-spacing: 2px; }
  .brand__name small { display: block; font-size: 17px; letter-spacing: 3px; }
  .card--front .brand { left: 58px; top: 72px; }
  .card--back .brand { right: 75px; top: 82px; }

  .front__web {
    position: absolute; right: 41px; top: 440px;
    font-family: "Nunito", sans-serif; font-size: 19px; color: var(--white);
    letter-spacing: 0.5px;
  }

  .accent-bar {
    position: absolute; left: 0; top: 204px; width: 15px; height: 74px;
    background: var(--yellow);
  }
  .person { position: absolute; left: 75px; top: 210px; color: var(--grey); font-family: "Montserrat", sans-serif; }
  .person__name { font-size: 36px; font-weight: 700; letter-spacing: 6px; line-height: 1; }
  .person__title { font-size: 21px; font-weight: 600; margin-top: 6px; }
  .divider {
    position: absolute; left: 75px; right: 75px; top: 293px; height: 2px;
    background: var(--rule);
  }
  .contacts { position: absolute; left: 75px; top: 318px; list-style: none; }
  .contacts li {
    display: flex; align-items: center; gap: 16px; height: 33px;
    font-family: "Nunito", sans-serif; font-size: 19px; color: var(--grey-light);
    letter-spacing: 0.5px;
  }
  .contacts .phone { letter-spacing: 3px; }
  .contacts svg { width: 25px; height: 25px; flex: none; }
  .address {
    position: absolute; right: 75px; top: 382px;
    font-family: "Nunito", sans-serif; font-size: 18px; color: var(--grey-light);
  }
</style>
</head>
<body>
  <section class="card card--front">
    <div class="brand">
      <span class="brand__mark"></span>
      <span class="brand__name">Bront<small>Engineering Qavo</small></span>
    </div>
    <p class="front__web">www.yourwebsite.com</p>
  </section>

  <section class="card card--back">
    <div class="brand">
      <span class="brand__mark brand__mark--grey"></span>
      <span class="brand__name">Bront<small>Engineering Qavo</small></span>
    </div>
    <span class="accent-bar"></span>
    <div class="person">
      <h1 class="person__name">Your Name</h1>
      <p class="person__title">Your Title</p>
    </div>
    <span class="divider"></span>
    <ul class="contacts">
      <li>
        <svg viewBox="0 0 24 24" aria-hidden="true"><circle cx="12" cy="12" r="12" fill="#a8a8a8"/><path d="M7.5 6.5l2-1 2 3-1.3 1.2c.7 1.6 1.9 2.8 3.5 3.5l1.2-1.3 3 2-1 2c-5 .3-9.7-4.4-9.4-9.4z" fill="#1c1c1c"/></svg>
        <span class="phone">123-456-789</span>
      </li>
      <li>
        <svg viewBox="0 0 24 24" aria-hidden="true"><circle cx="12" cy="12" r="12" fill="#a8a8a8"/><g fill="none" stroke="#1c1c1c" stroke-width="1.2"><circle cx="12" cy="12" r="6.5"/><ellipse cx="12" cy="12" rx="3" ry="6.5"/><path d="M5.5 12h13M6.5 9h11M6.5 15h11"/></g></svg>
        <span>www.yourwebsite.com</span>
      </li>
      <li>
        <svg viewBox="0 0 24 24" aria-hidden="true"><circle cx="12" cy="12" r="12" fill="#a8a8a8"/><g fill="none" stroke="#1c1c1c" stroke-width="1.2"><rect x="6" y="8" width="12" height="8"/><path d="M6 8l6 4.5L18 8M6 16l4.5-4M18 16l-4.5-4"/></g></svg>
        <span>email@info.com</span>
      </li>
    </ul>
    <p class="address">Your Address and Country</p>
  </section>
</body>
</html>
```